Business Card Design

Velvet Pixel Promotions

An online marketing consulting & strategy business for the cosmetic niche

We specialise in Increasing Leads, Conversions & Content Marketing

I am looking for a very clean, BOLD business card that is simple & effective

Target Market(s)

cosmetic surgeons & cosmetic clinics

Industry/Entity Type

Marketing

Contact Information for Business Card

Darren Okoye
Online Marketing Strategist

Darren@VelvetPixelPromotions.example
0491 268 517

LinkedIn: in/darrenokoye

```html
<!DOCTYPE html>
<html lang="en">
<head>
<meta charset="utf-8">
<title>Velvet Pixel Promotions — Business Card</title>
<link rel="stylesheet" href="https://fonts.googleapis.com/css2?family=Montserrat:wght@400;500;600&display=swap">
<style>
  :root {
    --bg: #e4e5e6;
    --green: #8cc63f;
    --teal: #13a6b4;
    --paper: #f7f7f5;
    --ink: #3a3b3d;
    --ink-soft: #55575a;
    --ring: #9a9ea3;
    --white: #ffffff;
  }
  * { margin: 0; padding: 0; box-sizing: border-box; }
  html, body {
    width: 1200px;
    height: 874px;
    overflow: hidden;
    background: var(--bg);
    font-family: "Montserrat", Arial, sans-serif;
  }
  .canvas {
    position: relative;
    width: 1200px;
    height: 874px;
  }
  .card {
    position: absolute;
    width: 560px;
    height: 320px;
    border-radius: 4px;
    overflow: hidden;
    box-shadow: 0 6px 18px rgba(0,0,0,0.18);
  }
  /* Front */
  .card-front {
    left: 570px;
    top: 90px;
    background: linear-gradient(160deg, var(--green) 0%, #4cb86a 45%, var(--teal) 100%);
    display: flex;
    align-items: center;
    justify-content: center;
  }
  .brand-front {
    display: flex;
    align-items: center;
    gap: 22px;
    color: var(--white);
  }
  .brand-front .brand-dot {
    width: 70px;
    height: 70px;
    border-radius: 50%;
    background: var(--white);
    flex: none;
  }
  .brand-front .brand-name {
    font-weight: 500;
    font-size: 34px;
    line-height: 1.05;
    letter-spacing: 3px;
    text-transform: uppercase;
  }
  /* Back */
  .card-back {
    left: 70px;
    top: 460px;
    background: var(--paper);
  }
  .card-back .sweep {
    position: absolute;
    inset: 0;
    width: 560px;
    height: 320px;
  }
  .card-back .brand-back {
    position: absolute;
    left: 34px;
    top: 30px;
    display: flex;
    align-items: center;
    gap: 10px;
  }
  .brand-back .brand-dot {
    width: 34px;
    height: 34px;
    border-radius: 50%;
    background: var(--teal);
    flex: none;
  }
  .brand-back .brand-name {
    font-weight: 600;
    font-size: 15px;
    line-height: 1.05;
    letter-spacing: 1.5px;
    text-transform: uppercase;
    color: var(--ink);
  }
  .person {
    position: absolute;
    left: 34px;
    top: 106px;
    color: var(--ink);
  }
  .person-name {
    font-weight: 600;
    font-size: 20px;
  }
  .person-role {
    font-weight: 400;
    font-size: 17px;
    color: var(--ink-soft);
    margin-top: 2px;
  }
  .contact {
    position: absolute;
    left: 34px;
    top: 190px;
    list-style: none;
    font-size: 15px;
    line-height: 1.45;
    color: var(--ink-soft);
  }
</style>
</head>
<body>
<main class="canvas">

  <section class="card card-front" aria-label="Business card front">
    <div class="brand-front">
      <span class="brand-dot"></span>
      <span class="brand-name">Velvet<br>Pixel<br>Promotions</span>
    </div>
  </section>

  <section class="card card-back" aria-label="Business card back">
    <svg class="sweep" viewBox="0 0 560 320" aria-hidden="true">
      <defs>
        <linearGradient id="sweepFill" x1="0" y1="0" x2="0.4" y2="1">
          <stop offset="0" stop-color="#8cc63f"/>
          <stop offset="0.5" stop-color="#4cb86a"/>
          <stop offset="1" stop-color="#13a6b4"/>
        </linearGradient>
      </defs>
      <rect x="0" y="0" width="560" height="320" fill="url(#sweepFill)"/>
      <ellipse cx="110" cy="250" rx="368" ry="330" fill="#a9adb2"/>
      <ellipse cx="100" cy="250" rx="362" ry="328" fill="#f7f7f5"/>
    </svg>

    <div class="brand-back">
      <span class="brand-dot"></span>
      <span class="brand-name">Velvet<br>Pixel<br>Promotions</span>
    </div>

    <div class="person">
      <p class="person-name">Darren Okoye</p>
      <p class="person-role">Online Marketing Specialist</p>
    </div>

    <ul class="contact">
      <li>Darren@VelvetPixelPromotions.example</li>
      <li>0491 268 517</li>
      <li>LinkedIn: in/darrenokoye</li>
    </ul>
  </section>

</main>
</body>
</html>
```